Pemberton Dialworks Business Card Design

Double Sided Business Card Design for a Locksmith company specializing in Safecracking, safe & vault service.

```html
<!DOCTYPE html>
<html lang="en">
<head>
<meta charset="UTF-8">
<title>Pemberton Dialworks Business Card</title>
<link rel="stylesheet" href="https://fonts.googleapis.com/css2?family=Work+Sans:wght@400;500;800&display=swap">
<style>
  :root {
    --brand-green: #237a3c;
    --ink: #111111;
    --paper: #ffffff;
    --stage: #1e1f1e;
  }
  * { margin: 0; padding: 0; box-sizing: border-box; }
  html, body {
    width: 1200px;
    height: 900px;
    overflow: hidden;
    background: var(--stage);
    font-family: "Work Sans", Arial, sans-serif;
  }
  .card-sheet {
    position: relative;
    width: 1200px;
    height: 900px;
  }
  .card {
    position: absolute;
    top: 296px;
    width: 540px;
    height: 308px;
    border-radius: 22px;
    overflow: hidden;
  }
  .card-front { left: 40px; background: var(--paper); }
  .card-back  { left: 620px; background: var(--brand-green); }

  .wordmark {
    font-weight: 800;
    text-transform: uppercase;
    line-height: 1;
    letter-spacing: 0.02em;
  }
  .card-front .wordmark {
    position: absolute;
    left: 72px;
    top: 40px;
    font-size: 30px;
    color: var(--brand-green);
  }
  .wordmark-mark {
    position: absolute;
    right: 48px;
    top: 96px;
    width: 170px;
    height: 170px;
    border-radius: 50%;
    background: var(--brand-green);
  }

  .contact-block {
    position: absolute;
    left: 48px;
    top: 112px;
    padding-left: 24px;
  }
  .accent-bar {
    position: absolute;
    left: 0;
    top: 2px;
    width: 8px;
    height: 34px;
    background: var(--brand-green);
  }
  .person-name {
    font-size: 20px;
    font-weight: 500;
    letter-spacing: 0.08em;
    text-transform: uppercase;
    color: var(--brand-green);
  }
  .person-role {
    font-size: 13px;
    color: var(--ink);
    margin-bottom: 14px;
  }
  .address-line,
  .contact-line {
    font-size: 13px;
    line-height: 1.5;
    color: var(--ink);
  }
  .contact-list { list-style: none; margin-top: 4px; }
  .contact-line {
    display: flex;
    align-items: center;
    gap: 7px;
  }
  .contact-icon {
    width: 11px;
    height: 11px;
    fill: none;
    stroke: var(--brand-green);
    stroke-width: 1.6;
  }

  .card-back .wordmark {
    position: absolute;
    left: 0;
    right: 0;
    top: 50%;
    transform: translateY(-50%);
    text-align: center;
    font-size: 34px;
    color: var(--paper);
  }
</style>
</head>
<body>
<main class="card-sheet">
  <section class="card card-front" aria-label="Business card front">
    <p class="wordmark">Pemberton Dialworks</p>
    <div class="wordmark-mark" aria-hidden="true"></div>

    <div class="contact-block">
      <span class="accent-bar" aria-hidden="true"></span>
      <h1 class="person-name">Jonah Whitfield</h1>
      <p class="person-role">Founder</p>
      <p class="address-line">418 Larkspur Avenue</p>
      <p class="address-line">Halden, OR 97140</p>
      <ul class="contact-list">
        <li class="contact-line">
          <svg class="contact-icon" viewBox="0 0 12 12" aria-hidden="true">
            <path d="M3 1 L5 3.5 L3.8 5 Q5 7.5 7 8.2 L8.5 7 L11 9 L9.5 11 Q3 10 1 2.5 Z"/>
          </svg>
          555 013 2846
        </li>
        <li class="contact-line">
          <svg class="contact-icon" viewBox="0 0 12 12" aria-hidden="true">
            <rect x="1" y="2.5" width="10" height="7"/>
            <path d="M1 2.5 L6 6.5 L11 2.5"/>
          </svg>
          info@pembertondial.com
        </li>
        <li class="contact-line">
          <svg class="contact-icon" viewBox="0 0 12 12" aria-hidden="true">
            <circle cx="6" cy="6" r="5"/>
            <ellipse cx="6" cy="6" rx="2.2" ry="5"/>
            <path d="M1 6 H11"/>
          </svg>
          www.pembertondial.com
        </li>
      </ul>
    </div>
  </section>

  <section class="card card-back" aria-label="Business card back">
    <p class="wordmark">Pemberton Dialworks</p>
  </section>
</main>
</body>
</html>
```